Web design for new streaming audio service

We need a homepage design for a new streaming audio service. Our company is called Olvantra, and we’re basically Vidorama for Audiobooks, Stand-Up Comedy, Lectures, Language Learning, etc. Essentially like Tunelark for everything audio EXCEPT music.
You don’t have to code the homepage (Design Only), but it should include 3 different designs to work with 1) Web; 2) Phones; 3) Tablets.
Below is a link to a mockup of the web version which gives a good idea of what elements we want. This is just a mockup and we want you to improve it.
Once you download the mockup, please refer to the more detailed instructions below:
The following outlines the design project for the Olvantra homepage. We have provided a rough mockup of the homepage layout that gives you a general idea of what we’re going for. There are a few elements that we are attached to, and many others where you have complete creative freedom to do whatever you think looks good.
The ZIP file includes the following:
* Mockup to see what we have in mind (olvantra-homepage-mockup.jpg)
* Text used (olvantra-homepage-text.txt)
* Raw image of actor (olvantra-actor1.jpg)
* Raw images for samples (olvantra-sample-[name].jpg)
Although we have only provided a mockup layout for the web version, we also need you to provide a mobile phone and a tablet version of the design also. It’s very possible the tablet version may be substantially similar to the web version, but the mobile phone version will likely be much different.
All of the raw files are included in the attached ZIP file. Please use our photographs and text as provided although cropping, sizing, etc. is flexible per the instructions below.
Display Requirements:
* Web Version - Minimum resolution 1024x768 (72 dpi) but should look good on 1920x1080 (72 dpi) - Page should be designed to scale to look acceptable in all resolutions in between.
* Phone Version - Minimum Zentro 4 - 640x960 (326 dpi) but should look good on Korvel Nimbus Q5 - 1920x1080 (441 dpi) - Page should be designed to scale to look acceptable in all resolutions and devices in between.
* Tablet Version - Minimum Pagewick Ember LX 7” - 1280x800 (216 dpi) but should also look good on a Slato Breeze - 2048x1536 (264 dpi) - Page should be designed to scale to look acceptable in all resolutions and devices in between.
Above the Fold - We want to make sure the Olvantra logo, Member Login Link, Large Photo, Headline, Price, Button, and the first row of sample images are all “Above the fold”. As a general guideline, this means 600 pixels high on a 1024x768 72 dpi web screen. This requirement is less important on Phone versions.
Top Logo Bar - We want to retain the blue bar with the Olvantra logo on the page, although we are open to a different size, shape and positioning if it greatly enhances the design. Please use the standard logo color, although you are welcome to use either the horizontal or vertical orientation of the logo based on your design.
Text color, font and size - Feel free to design the text in anyway you choose as long as the text is readable on the target platforms.
Buttons - Feel free to use any size, shape and colors for the buttons as long as they are obvious and clickable relative to the page. The only exception is the Chatterly button should follow the Chatterly color scheme and logo treatment (the mockup doesn’t seem 100% correct.)
Top Photograph - We want to retain the large photograph across the top of the screen although final shape and dimensions are flexible.
Size and shape of content samples (i.e. Audiobooks, Stand-Up Comedy, etc.) - Feel free to design the content samples in anyway you choose.
Three Sales Points (i.e. Listen on your Zentro…, All you can enjoy…, etc.) - The Three Sales Points are envisioned to each have a corresponding illustration which you should provide and have rights for. The placeholder is represented by a square next to the text. The color size and shape of these elements are flexible and can be designed in any way you choose.
Opt-in form - Feel free to design the opt-in form in anyway you choose as long as the text is readable and the interactivity is obvious on the target platforms.
Text links and copyright notice - Feel free to design the bottom of the page text links and copyright notice in anyway you choose.
Additional colors, graphic design elements, etc. - Feel free to use any additional colors, graphic design elements, etc. to support your design.

```html
<!DOCTYPE html>
<html lang="en">
<head>
<meta charset="utf-8">
<title>Olvantra — Unlimited Listening</title>
<link rel="stylesheet" href="https://fonts.googleapis.com/css2?family=Signika:wght@400;600&family=Open+Sans:wght@400;600;700&display=swap">
<style>
:root{
  --bar-top:#5aa6d2;
  --bar-bottom:#3b86b8;
  --headline:#4f74a6;
  --teal:#3aa3b6;
  --green:#4dbb6b;
  --green-light:#72cf8d;
  --blue-link:#4ea3d4;
  --blue-heading:#2a74a4;
  --page:#ededec;
  --rule:#d9d9d9;
  --ink:#222;
  --muted:#666;
  --grey-btn:#8c8c8c;
  --dark:#404040;
  --social:#5b68a8;
  --social-dark:#4a5794;
}
*{box-sizing:border-box;margin:0;padding:0}
html,body{width:1200px;height:2344px;overflow:hidden}
body{background:var(--page);font-family:"Open Sans",sans-serif;color:var(--ink);position:relative}
.abs{position:absolute}

.topbar{left:0;top:0;width:1200px;height:94px;background:linear-gradient(var(--bar-top),var(--bar-bottom))}
.brand{left:38px;top:18px;display:flex;align-items:center;gap:14px;color:#fff;font-family:"Signika",sans-serif;font-weight:600;font-size:44px}
.brand-dot{width:48px;height:48px;border-radius:50%;background:#fff}
.menu-label{left:1000px;top:30px;color:#fff;font-weight:700;font-size:26px}
.menu-btn{left:1093px;top:19px;width:70px;height:56px;border-radius:6px;background:#2f79a8;border:2px solid #6cb2dc}
.menu-btn span{position:absolute;left:15px;width:36px;height:5px;background:#fff;border-radius:2px}

.hero{left:0;top:94px;width:1200px;height:502px;background:#fff;overflow:hidden}
.hero-photo{position:absolute;left:0;top:0;width:1200px;height:502px;
  background:linear-gradient(90deg,#ffffff 0%,#ffffff 38%,#e9e4df 55%,#c9b3a0 72%,#8a7a6e 88%,#5d6a7a 100%)}
.hero-fade{position:absolute;left:0;bottom:0;width:1200px;height:60px;background:linear-gradient(rgba(237,237,236,0),var(--page))}
.headline{font-family:"Signika",sans-serif;font-weight:400;color:var(--headline);font-size:64px;line-height:1;white-space:nowrap}
.price{left:126px;top:266px;color:var(--teal);font-family:"Signika",sans-serif;font-size:33px;line-height:1;white-space:nowrap}
.price .cur{font-size:30px;color:var(--green);vertical-align:46px;margin-left:8px}
.price .big{font-size:90px;font-weight:600;color:var(--green)}
.price .cents{font-size:40px;color:var(--green);margin-right:8px}
.cta{left:90px;top:376px;width:435px;height:67px;background:var(--green);color:#fff;font-family:"Signika",sans-serif;font-size:38px;display:flex;align-items:center;justify-content:center;border-radius:3px}
.cta-note{left:90px;top:448px;width:435px;text-align:center;font-size:18px;color:#555}

.section-title{left:38px;top:616px;font-family:"Signika",sans-serif;font-weight:400;color:var(--blue-heading);font-size:37px}
.dot{top:636px;width:22px;height:22px;border-radius:50%;background:#bcbcbc}
.rule{left:38px;width:1124px;height:2px;background:var(--rule)}

.sample-art{width:346px;height:346px;border-radius:50%;top:712px}
.sample-title{width:390px;text-align:center;top:1090px;font-family:"Signika",sans-serif;font-weight:600;font-size:29px;color:#333}
.sample-text{width:390px;text-align:center;top:1140px;font-size:23px;line-height:36px;color:var(--muted)}
.more{top:1232px;width:208px;height:58px;background:var(--grey-btn);color:#fff;font-weight:700;font-size:20px;display:flex;align-items:center;justify-content:center}

.card{top:1358px;width:350px;height:347px;background:#fff;box-shadow:0 2px 4px rgba(0,0,0,.12)}
.card-art{position:absolute;left:85px;top:44px;width:180px;height:180px;border-radius:6px;background:linear-gradient(#d9dee3,#c3cad1)}
.card p{position:absolute;left:0;top:268px;width:100%;text-align:center;font-size:18px;line-height:24px;color:#333}
.card b{color:var(--blue-link);font-weight:600}

.signup{left:32px;top:1772px;width:1125px;height:189px;background:linear-gradient(var(--green-light),var(--green))}
.signup h2{position:absolute;left:38px;top:18px;color:#fff;font-family:"Signika",sans-serif;font-weight:600;font-size:42px}
.email{position:absolute;left:36px;top:90px;width:798px;height:66px;background:#fff;border-radius:4px;display:flex;align-items:center;gap:18px;padding-left:20px;font-size:28px;color:#999}
.signup-btn{position:absolute;left:876px;top:90px;width:211px;height:66px;background:#3d3d3d;border-radius:4px;color:#fff;font-weight:700;font-size:25px;display:flex;align-items:center;justify-content:center}
.terms{left:32px;top:1961px;width:1125px;height:117px;background:var(--dark);color:#fff;font-size:24.5px;line-height:40px;padding:16px 0 0 36px}
.terms .brandword{color:var(--blue-link);font-weight:700}
.terms .days{color:var(--green-light);font-weight:700}
.terms .soft{color:#b5b5b5}

.access{left:32px;top:2111px;width:517px;height:60px;background:var(--grey-btn);color:#fff;font-weight:700;font-size:20px;display:flex;align-items:center}
.access .ico{width:62px;height:60px;background:#6e6e6e;display:flex;align-items:center;justify-content:center}
.access .lbl{flex:1;text-align:center}
.or{left:578px;top:2124px;font-weight:700;font-size:25px;color:#444}
.social{left:638px;top:2111px;width:519px;height:60px;background:var(--social);color:#fff;font-weight:700;font-size:20px;display:flex;align-items:center}
.social .ico{width:62px;height:60px;background:var(--social-dark)}
.social .lbl{flex:1;text-align:center}

.copyright{left:0;top:2228px;width:1200px;text-align:center;font-size:25px;color:#333}
.links{left:0;top:2283px;width:1200px;text-align:center;font-size:25px;color:#666}
</style>
</head>
<body>
<header class="abs topbar"></header>
<div class="abs brand"><span class="brand-dot"></span>Olvantra</div>
<div class="abs menu-label">MENU</div>
<div class="abs menu-btn"><span style="top:12px"></span><span style="top:25px"></span><span style="top:38px"></span></div>

<section class="abs hero">
  <div class="hero-photo" role="img" aria-label="Smiling young man wearing headphones, looking at his phone"></div>
  <div class="hero-fade"></div>
</section>
<h1 class="abs headline" style="left:36px;top:130px">Unlimited Listening.</h1>
<div class="abs headline" style="left:60px;top:210px">Wherever you are.</div>
<div class="abs price">Only<span class="cur">$</span><span class="big">9</span><span class="cents">.99</span>per month</div>
<div class="abs cta">Start Your Free Trial</div>
<div class="abs cta-note">* Credit Card Not Required</div>

<h2 class="abs section-title">A sample of what you can listen to on Olvantra</h2>
<span class="abs dot" style="left:1028px;background:var(--blue-link)"></span>
<span class="abs dot" style="left:1063px"></span>
<span class="abs dot" style="left:1101px"></span>
<span class="abs dot" style="left:1137px"></span>
<div class="abs rule" style="top:683px"></div>

<div class="abs sample-art" style="left:37px;background:radial-gradient(circle,#5a5d62,#1e2024)" role="img" aria-label="Audiobook cover art for a suspense novel collection"></div>
<div class="abs sample-art" style="left:425px;background:radial-gradient(circle,#8a6a50,#3e3230)" role="img" aria-label="Comedy album art showing a boxing ring"></div>
<div class="abs sample-art" style="left:815px;background:radial-gradient(circle,#2d8fb6,#123a5a)" role="img" aria-label="French language course cover art"></div>

<h3 class="abs sample-title" style="left:15px;color:var(--blue-link)">Audiobooks</h3>
<h3 class="abs sample-title" style="left:403px">Stand-Up Comedy</h3>
<h3 class="abs sample-title" style="left:793px">Language Learning</h3>
<p class="abs sample-text" style="left:15px;color:#222">Lorem ipsum dolor sit amet,<br>consectetuer adipiscing elit.</p>
<p class="abs sample-text" style="left:403px">Lorem ipsum dolor sit amet,<br>consectetuer adipiscing elit.</p>
<p class="abs sample-text" style="left:793px">Lorem ipsum dolor sit amet,<br>consectetuer adipiscing elit.</p>
<div class="abs more" style="left:107px;background:var(--blue-link)">MORE DETAILS</div>
<div class="abs more" style="left:490px">MORE DETAILS</div>
<div class="abs more" style="left:881px">MORE DETAILS</div>
<div class="abs rule" style="top:1323px"></div>

<div class="abs card" style="left:36px">
  <div class="card-art" role="img" aria-label="Illustration of a tablet and a phone showing the app"></div>
  <p>Listen on your <b>Zentro</b>, <b>Slato</b><br>or <b>Orbitos</b> device.</p>
</div>
<div class="abs card" style="left:428px">
  <div class="card-art" role="img" aria-label="Illustration of headphones with a price symbol"></div>
  <p>All you can enjoy for<br>one <b>low</b> monthly <b>price</b>.</p>
</div>
<div class="abs card" style="left:814px">
  <div class="card-art" role="img" aria-label="Illustration of an alarm clock marked with a cross"></div>
  <p>No obligation.<br>Cancel any <b>time</b>.</p>
</div>
<div class="abs rule" style="top:1740px"></div>

<section class="abs signup">
  <h2>Start Your Free Trial</h2>
  <div class="email">
    <svg width="40" height="28" viewBox="0 0 40 28"><rect width="40" height="28" fill="#888"/><path d="M0 0 L20 16 L40 0" fill="none" stroke="#fff" stroke-width="3"/></svg>
    Your Email Adress
  </div>
  <div class="signup-btn">SIGN UP</div>
</section>
<p class="abs terms">You will get instant &amp; unlimited access to all the material on <span class="brandword">Olvantra</span> for <span class="days">14 days</span>.<br>There is <b>no obligation</b> &amp; you can cancel at <b>any time</b>. <span class="soft">Credit Card Not Required for Free Trial.</span></p>

<div class="abs access">
  <span class="ico"><svg width="22" height="26" viewBox="0 0 22 26"><path d="M5 12 V8 a6 6 0 0 1 12 0 V12" fill="none" stroke="#fff" stroke-width="3"/><rect x="1" y="11" width="20" height="15" rx="2" fill="#fff"/></svg></span>
  <span class="lbl">GET INSTANT ACCESS</span>
</div>
<div class="abs or">OR</div>
<div class="abs social"><span class="ico"></span><span class="lbl">SIGN UP USING CHATTERLY</span></div>

<p class="abs copyright">© 2014 <b>Olvantra LLC</b> - All Rights Reserved</p>
<nav class="abs links">About | Help | Contact Us | Member Login | Privacy Policy | Terms of Service</nav>
</body>
</html>
```